Need Flyer for Our Real estate Agency

Need to run General Campaign for our agency with Start of New Year as our theme ..Must have an agent's picture on the DL..
Address:
9 / 386Barwin rd, Truganina VIC 3029
Ph:03 9142 7305
email:info@koridanrealestate.example.au
www.koridanrealestate.example.au
Something like as attached picture..
Target Market(s)
Home Buyers
Industry/Entity Type
Real Estate Agent
Requirements
Must have
- Our Logo Colours

```html
<!DOCTYPE html>
<html lang="en">
<head>
<meta charset="utf-8">
<title>Koridan Real Estate – New Year DL Flyer</title>
<link href="https://fonts.googleapis.com/css2?family=Montserrat:wght@700&family=Lato:wght@400;700&display=swap" rel="stylesheet">
<style>
  :root {
    --navy: #13205a;
    --navy-soft: #2a3a78;
    --accent-red: #7a1c24;
    --white: #ffffff;
    --paper: #f7f8fa;
    --backdrop: #e9e9ea;
  }
  * { box-sizing: border-box; margin: 0; padding: 0; }
  html, body {
    width: 1200px; height: 1200px; overflow: hidden;
    background: var(--backdrop);
  }
  .flyer {
    position: absolute;
    left: 40px; top: 333px;
    width: 1120px; height: 534px;
    display: flex;
    box-shadow: 0 14px 40px rgba(0,0,0,0.18);
  }
  .agent-photo {
    width: 400px; height: 100%;
    background: linear-gradient(180deg, var(--paper) 0%, var(--paper) 22%, #c9cfe0 45%, var(--navy-soft) 70%, var(--navy) 100%);
  }
  .campaign-panel {
    position: relative;
    flex: 1;
    background: var(--navy);
    color: var(--white);
    padding: 46px 56px 0 40px;
    text-align: right;
  }
  .brand {
    display: inline-flex; align-items: center; gap: 12px;
    font-family: "Lato", sans-serif;
    font-weight: 700;
    font-size: 30px;
    letter-spacing: 4px;
    color: var(--white);
    margin-top: 40px;
  }
  .brand-mark {
    width: 14px; height: 14px;
    background: var(--white);
  }
  .headline {
    margin-top: 58px;
    font-family: "Montserrat", sans-serif;
    font-weight: 700;
    font-size: 36px;
    line-height: 1.3;
  }
  .headline-rule {
    display: block;
    width: 440px; height: 11px;
    margin: 14px -20px 0 auto;
    background: var(--accent-red);
  }
  .contact-list {
    list-style: none;
    margin-top: 26px;
    font-family: "Lato", sans-serif;
    font-size: 21px;
  }
  .contact-item {
    display: flex; justify-content: flex-end; align-items: center;
    gap: 14px;
    margin-bottom: 12px;
  }
  .contact-item.is-online { letter-spacing: 1.5px; }
  .contact-icon { width: 24px; height: 24px; flex: none; }
</style>
</head>
<body>
  <section class="flyer">
    <div class="agent-photo" role="img" aria-label="Portrait of a smiling real estate agent in a navy suit with arms crossed, on a white background"></div>

    <div class="campaign-panel">
      <div class="brand"><span class="brand-mark"></span>KORIDAN REAL ESTATE</div>

      <h1 class="headline">Start your New Year with<br>knowing the value of your property</h1>
      <span class="headline-rule"></span>

      <ul class="contact-list">
        <li class="contact-item">
          <span>9 / 386Barwin rd, Truganina VIC 3029</span>
          <svg class="contact-icon" viewBox="0 0 24 24"><circle cx="12" cy="12" r="12" fill="#fff"/><path d="M12 5a4.5 4.5 0 0 0-4.5 4.5C7.5 13 12 19 12 19s4.5-6 4.5-9.5A4.5 4.5 0 0 0 12 5z" fill="#13205a"/><circle cx="12" cy="9.5" r="1.6" fill="#fff"/></svg>
        </li>
        <li class="contact-item">
          <span>03 9142 7305</span>
          <svg class="contact-icon" viewBox="0 0 24 24"><circle cx="12" cy="12" r="12" fill="#fff"/><path d="M8.2 6.5l2 2.4-1.1 1.5a8 8 0 0 0 4.5 4.5l1.5-1.1 2.4 2-1.2 1.9C11.5 17.6 6.4 12.5 6.3 7.7z" fill="#13205a"/></svg>
        </li>
        <li class="contact-item is-online">
          <span>info@koridanrealestate.example.au</span>
          <svg class="contact-icon" viewBox="0 0 24 24"><circle cx="12" cy="12" r="12" fill="#fff"/><rect x="6" y="8" width="12" height="8.5" rx="1" fill="#13205a"/><path d="M6.5 8.8L12 13l5.5-4.2" stroke="#fff" stroke-width="1.2" fill="none"/></svg>
        </li>
        <li class="contact-item is-online">
          <span>www.koridanrealestate.example.au</span>
          <svg class="contact-icon" viewBox="0 0 24 24"><circle cx="12" cy="12" r="12" fill="#fff"/><circle cx="12" cy="12" r="6" fill="none" stroke="#13205a" stroke-width="1.5"/><ellipse cx="12" cy="12" rx="2.6" ry="6" fill="none" stroke="#13205a" stroke-width="1.3"/><path d="M6 12h12" stroke="#13205a" stroke-width="1.3"/></svg>
        </li>
      </ul>
    </div>
  </section>
</body>
</html>
```